Birchlane Chiropractic Business Cards

Business cards with new logo design. Will upload copy of current card. We like the layout, but we need a new logo. Family, husband holding up baby toward sky, mom and other child standing next to him. We will probably want to include a catch phrase with logo. TBD

```html
<!DOCTYPE html>
<html lang="en">
<head>
<meta charset="utf-8">
<title>Birchlane Chiropractic Business Cards</title>
<link rel="stylesheet" href="https://fonts.googleapis.com/css2?family=Poppins:wght@400;500;600;700;800&display=swap">
<style>
  :root {
    --red: #ec2027;
    --red-deep: #b8161c;
    --black: #111111;
    --white: #ffffff;
    --ink: #1a1a1a;
    --stage: #2b2b2b;
    --sun: #f4d21f;
  }
  * { box-sizing: border-box; margin: 0; padding: 0; }
  html, body { width: 1200px; height: 1108px; overflow: hidden; }
  body {
    background: var(--stage);
    font-family: "Poppins", sans-serif;
    position: relative;
  }
  .card {
    position: absolute;
    top: 174px;
    width: 440px;
    height: 760px;
    border-radius: 22px;
    overflow: hidden;
  }
  .card-front { left: 130px; background: var(--white); }
  .card-back { left: 630px; background: var(--red); }
  .card-bg { position: absolute; inset: 0; }

  .emblem {
    position: absolute;
    left: 105px; top: 48px;
    width: 230px; height: 230px;
    border-radius: 50%;
    background: var(--sun);
    border: 8px solid var(--white);
  }
  .brand-name {
    position: absolute;
    left: 0; right: 0;
    text-align: center;
    font-weight: 800;
    text-transform: uppercase;
    line-height: 1;
  }
  .card-front .brand-name { top: 300px; color: var(--red); }
  .brand-name .line-1 { display: block; font-size: 50px; letter-spacing: 1px; }
  .brand-name .line-2 { display: block; font-size: 34px; letter-spacing: 1px; margin-top: 6px; }

  .doctor {
    position: absolute; top: 408px; left: 0; right: 0; text-align: center;
  }
  .doctor-name { font-size: 22px; font-weight: 700; color: var(--ink); }
  .doctor-title { font-size: 17px; font-weight: 500; color: var(--red); margin-top: 2px; }

  .divider {
    display: flex; align-items: center; justify-content: center; gap: 8px;
    margin: 10px auto 6px;
  }
  .divider .rule { width: 50px; height: 2px; background: var(--red); }
  .divider svg { width: 14px; height: 14px; fill: var(--red); }

  .contact {
    position: absolute; top: 478px; left: 0; right: 0;
    text-align: center; color: var(--ink);
    font-size: 16px; line-height: 1.4;
  }
  .contact .address { font-size: 15px; line-height: 1.35; }

  .map-area {
    position: absolute;
    left: 36px; top: 50px;
    width: 368px; height: 380px;
    border-radius: 6px;
    background: var(--red-deep);
    opacity: 0.85;
  }
  .card-back .brand-name { top: 520px; color: var(--white); }
  .card-back .brand-name .line-1 { font-size: 52px; }
  .card-back .brand-name .line-2 { font-size: 36px; }
  .back-phone {
    position: absolute; top: 636px; left: 0; right: 0;
    display: flex; justify-content: center; align-items: center; gap: 10px;
    color: var(--white); font-size: 26px; font-weight: 500;
  }
  .back-phone svg { width: 22px; height: 22px; fill: var(--white); }
</style>
</head>
<body>

<section class="card card-front">
  <svg class="card-bg" viewBox="0 0 440 760" preserveAspectRatio="none" aria-hidden="true">
    <polygon points="0,0 440,0 440,170 0,240" fill="var(--red)"/>
    <polygon points="170,760 440,760 440,610" fill="var(--black)"/>
    <polygon points="0,690 0,760 170,760" fill="var(--white)"/>
  </svg>

  <div class="emblem" role="img" aria-label="Emblem area for the practice mark"></div>

  <h1 class="brand-name">
    <span class="line-1">Birchlane</span>
    <span class="line-2">Chiropractic</span>
  </h1>

  <div class="doctor">
    <p class="doctor-name">Dr. Daniel R. Ostrander</p>
    <p class="doctor-title">Chiropractic Physician</p>
  </div>

  <div class="contact">
    <div class="divider">
      <span class="rule"></span>
      <svg viewBox="0 0 24 24" aria-hidden="true"><path d="M6.6 10.8a15.1 15.1 0 0 0 6.6 6.6l2.2-2.2a1 1 0 0 1 1-.25 11.4 11.4 0 0 0 3.6.57 1 1 0 0 1 1 1V20a1 1 0 0 1-1 1A17 17 0 0 1 3 4a1 1 0 0 1 1-1h3.5a1 1 0 0 1 1 1c0 1.25.2 2.45.57 3.6a1 1 0 0 1-.25 1z"/></svg>
      <svg viewBox="0 0 24 24" aria-hidden="true"><rect x="6" y="3" width="12" height="5"/><rect x="3" y="9" width="18" height="8" rx="2"/><rect x="6" y="14" width="12" height="7"/></svg>
      <svg viewBox="0 0 24 24" aria-hidden="true"><circle cx="12" cy="12" r="10"/></svg>
      <span class="rule"></span>
    </div>
    <p>503-555-0142</p>
    <p>503-555-0178</p>
    <p>www.Ostranderchiropractic.com</p>
    <div class="divider">
      <span class="rule"></span>
      <svg viewBox="0 0 24 24" aria-hidden="true"><path d="M12 2a7 7 0 0 0-7 7c0 5 7 13 7 13s7-8 7-13a7 7 0 0 0-7-7zm0 9.5A2.5 2.5 0 1 1 12 6.5a2.5 2.5 0 0 1 0 5z"/></svg>
      <span class="rule"></span>
    </div>
    <p class="address">4820 SE Maple Grove Center Dr.<br>Maple Grove, Oregon 97015</p>
  </div>
</section>

<section class="card card-back">
  <svg class="card-bg" viewBox="0 0 440 760" preserveAspectRatio="none" aria-hidden="true">
    <polygon points="250,0 440,0 440,560 360,760" fill="var(--black)"/>
  </svg>

  <div class="map-area" role="img" aria-label="Street map showing the clinic location between nearby roads and landmarks"></div>

  <h2 class="brand-name">
    <span class="line-1">Birchlane</span>
    <span class="line-2">Chiropractic</span>
  </h2>

  <p class="back-phone">
    <svg viewBox="0 0 24 24" aria-hidden="true"><path d="M6.6 10.8a15.1 15.1 0 0 0 6.6 6.6l2.2-2.2a1 1 0 0 1 1-.25 11.4 11.4 0 0 0 3.6.57 1 1 0 0 1 1 1V20a1 1 0 0 1-1 1A17 17 0 0 1 3 4a1 1 0 0 1 1-1h3.5a1 1 0 0 1 1 1c0 1.25.2 2.45.57 3.6a1 1 0 0 1-.25 1z"/></svg>
    503-555-0190
  </p>
</section>

</body>
</html>
```